Brisk Tutorium Website

We are looking for a new design of our website. The current website is www.brisktutorium.example. The company is the #1 pre-college math and science program in Orange County, CA. We would like to see designs that integrate our logo with a modern color scheme. We are also open for suggestions that could improve our logo. We would like a simple, minimal, clean, classy, and vibrant front-page user interface design that give the premium, modern, innovative, creative, and premier brand feel. We like the "New Retro Colors for the Web" as described here: http://www.pixel-layoutnook.example/en/layout-notes-2013/.

Target Market(s)

The target market is parents with K-12 students from a diverse population. Parents are well educated with family income > $150,000. Most of the decision makers are mothers from immigrate families: 30% Chinese, 30% Korean, 15% Indian, 24% White.

Industry/Entity Type

College

Requirements
Must have
• Must read our statement of differentiation at:
• http://brisktutorium.example/about-us
• Your design must be reflective of your understanding of the statements.
Nice to have
• The design should also be mobil friendly.
Should not have
• While most of our current classes are math, our company is expanding to include STEM (Science, Technology, Engineering, and Math) for gifted students. Therefore, the site should not be JUST a math education site.

```html
<!DOCTYPE html>
<html lang="en">
<head>
<meta charset="utf-8">
<title>Brisk Tutorium for Gifted Youth</title>
<link href="https://fonts.googleapis.com/css2?family=PT+Sans+Narrow:wght@400;700&family=Source+Sans+3:wght@400;600;700&display=swap" rel="stylesheet">
<style>
:root{
  --page-green:#8dc38b;
  --footer-green:#5f9a5c;
  --footer-dark:#2f2f2f;
  --navy:#1f2a78;
  --nav-top:#34628f;
  --nav-bottom:#1c3d62;
  --text:#444;
  --muted:#666;
  --link-green:#3b9a2e;
  --link-navy:#1f3a8a;
  --teal-top:#80c3c3;
  --teal-bottom:#48a6a7;
  --reg-green:#7cc07a;
  --panel-grey:#ececec;
  --cell:#dcdcdc;
  --cell-hi:#4aa3c0;
  --card-border:#dcdcdc;
}
*{box-sizing:border-box;margin:0;padding:0}
html,body{width:846px;height:1200px;overflow:hidden}
body{background:var(--page-green);font-family:"Source Sans 3",sans-serif;color:var(--text);position:relative}
.abs{position:absolute}
.top-links{right:70px;top:12px;font:700 11px "PT Sans Narrow",sans-serif;color:#2a3a2a;letter-spacing:.3px}
.sheet{left:70px;top:38px;width:706px;height:934px;background:#fff}
.brand{left:80px;top:56px;display:flex;align-items:center;gap:8px}
.brand-dot{width:26px;height:26px;border-radius:50%;background:#3f8fcf}
.brand-name{font:600 21px "Source Sans 3",sans-serif;color:var(--navy)}
.search{left:576px;top:61px;width:192px;height:25px;border:1px solid #ccc;border-radius:2px;font-size:10px;color:#999;padding:6px 13px}
.search-btn{position:absolute;right:2px;top:2px;width:19px;height:19px;background:#999;border-radius:2px}
.main-nav{left:78px;top:112px;width:691px;height:31px;display:flex;background:linear-gradient(var(--nav-top),var(--nav-bottom));border-radius:3px}
.main-nav a{display:flex;align-items:center;justify-content:center;color:#fff;font:700 11.5px "PT Sans Narrow",sans-serif;text-decoration:none;border-right:1px solid #17334f;height:100%}
.main-nav a:last-child{border-right:0}
.hero{left:78px;top:149px;width:691px;height:228px;background:var(--panel-grey);border:1px solid #ddd}
.slide{left:85px;top:157px;width:477px;height:212px;background:linear-gradient(90deg,#b9b9bf,#a9a9b1 55%,#bebec4);border-radius:3px}
.slide-title{left:378px;top:210px;width:180px;font:700 15px/22px "Source Sans 3",sans-serif;color:#3a3a3a}
.slide-arrow{width:19px;height:19px;border-radius:50%;background:#fff;top:338px}
.cal-title{left:575px;top:156px;width:190px;text-align:center;font:600 16px "Source Sans 3",sans-serif;color:#2f3f96}
.cal-head{left:575px;top:184px;width:189px;height:30px;background:#333;color:#fff;display:flex;justify-content:space-between;align-items:center;padding:0 10px;font:600 14px "Source Sans 3",sans-serif}
.cal-head span.arr{font-size:9px}
.cal-days,.cal-grid{left:576px;width:188px;display:grid;grid-template-columns:repeat(7,1fr);gap:1px;text-align:center}
.cal-days{top:219px;font:600 7.5px "Source Sans 3",sans-serif;color:#555}
.cal-grid{top:231px}
.cal-grid div{height:26px;background:var(--cell);display:flex;align-items:center;justify-content:center;font:600 11px "Source Sans 3",sans-serif;color:#444;border-radius:1px}
.cal-grid .off{color:#aaa;background:#e8e8e8}
.cal-grid .today{background:var(--cell-hi);color:#cde}
h2{font:600 16px "Source Sans 3",sans-serif;color:var(--navy)}
.copy{font-size:10.2px;line-height:17.6px;color:var(--text)}
.card{width:156px;height:100px;border:1px solid var(--card-border);top:504px;padding:8px 12px}
.card h3{display:flex;align-items:center;gap:8px;font:600 14px "Source Sans 3",sans-serif;color:var(--navy);margin-bottom:10px}
.card .ico{width:18px;height:18px;background:#3a3a3a;border-radius:2px;display:inline-block}
.card p{font-size:9px;line-height:14.5px;color:var(--muted)}
.doc-link{left:92px;display:flex;align-items:center;gap:14px;font:600 14px "Source Sans 3",sans-serif;color:#666}
.col-rule{left:580px;top:394px;width:1px;height:372px;background:#e3e3e3}
.news-nav{left:750px;top:398px;font-size:12px;color:#888;letter-spacing:2px}
.news{left:598px;top:428px;width:171px;height:176px;border:1px solid #ddd;padding:8px 12px}
.news li{list-style:none;margin-bottom:11px;font-size:9.6px;line-height:16px;padding-left:15px;position:relative}
.news li::before{content:"»";position:absolute;left:0;color:var(--link-green);font-size:12px}
.news a{color:var(--link-green);text-decoration:none}
.news time{color:#555;display:block}
.venue{left:598px;top:612px;width:171px;height:154px;border:1px solid #ddd;padding:10px 14px;font-size:9.6px;line-height:16px}
.venue-badge{width:150px;height:40px;background:#e6e6e6;margin:0 -4px 6px}
.venue a{color:var(--link-navy);text-decoration:none;display:block;margin-top:3px}
.why{left:78px;top:778px;width:691px;height:127px;background:linear-gradient(var(--teal-top),var(--teal-bottom));padding:14px 16px;color:#fff}
.why h2{color:#fff;font-size:16px;margin-bottom:8px}
.why p{font-size:9.8px;line-height:17.6px}
.reg-title{left:88px;top:923px;font:600 19.5px "Source Sans 3",sans-serif;color:var(--reg-green)}
.reg-note{left:318px;top:921px;font-size:9.8px;line-height:16.5px;color:#444}
.reg-btn{left:587px;top:920px;width:145px;height:32px;background:linear-gradient(#555,#2b2b2b);border-radius:3px;color:#fff;font:700 14px "PT Sans Narrow",sans-serif;display:flex;align-items:center;justify-content:center;gap:8px}
.reg-btn i{width:16px;height:16px;border-radius:50%;background:#777;display:inline-flex;align-items:center;justify-content:center;font-style:normal;font-size:10px}
.footer{left:0;top:986px;width:846px;height:168px;background:var(--footer-green);border-top:2px solid #4b8648;color:#fff}
.footer h4{font:400 13px/16px "Source Sans 3",sans-serif;margin-bottom:10px}
.f-col{position:absolute;top:13px}
.f-col ul{list-style:none}
.f-col li{font-size:9px;line-height:20.6px}
.f-col li::before{content:"• "}
.f-rule{position:absolute;top:14px;width:1px;height:144px;background:#4d874a}
.field{width:160px;height:20px;background:#f2f2f2;border:1px solid #ccc;color:#333;font-size:8.5px;padding:4px 11px;margin-bottom:10px}
.submit{margin-left:110px;width:50px;height:20px;background:#333;border:1px solid #111;font:700 10px "PT Sans Narrow",sans-serif;display:flex;align-items:center;justify-content:center}
.social li{list-style:none;display:flex;align-items:center;gap:12px;font-size:9.6px;height:29.5px}
.social li::before{content:none}
.social b{font-weight:400;font-size:11.5px}
.social .sq{width:19px;height:19px;background:#3d6aa8;border-radius:2px}
.bottom-bar{left:0;top:1154px;width:846px;height:46px;background:var(--footer-dark);color:#bbb;font-size:9.6px;text-align:center;line-height:46px}
</style>
</head>
<body>
<div class="abs top-links">REGISTER &nbsp;::&nbsp; LOGIN</div>
<div class="abs sheet"></div>

<div class="abs brand"><span class="brand-dot"></span><span class="brand-name">Brisk Tutorium</span></div>
<div class="abs search">Search<span class="search-btn"></span></div>

<nav class="abs main-nav">
  <a style="width:63px" href="#">HOME</a><a style="width:73px" href="#">ABOUT US</a><a style="width:71px" href="#">SUBJECTS</a><a style="width:86px" href="#">SCIENCE FAIR</a><a style="width:72px" href="#">FALL 2013</a><a style="width:88px" href="#">SUMMER 2013</a><a style="width:67px" href="#">RESULTS</a><a style="width:93px" href="#">ACCESSIBILITY</a><a style="width:78px" href="#">CONTACT</a>
</nav>

<div class="abs hero"></div>
<div class="abs slide" role="img" aria-label="Photo of an instructor writing math formulas on a glass board"></div>
<div class="abs slide-title">Math Olympiad and Problem Solving Training Programs</div>
<svg class="abs slide-arrow" style="left:512px" viewBox="0 0 19 19"><circle cx="9.5" cy="9.5" r="9.5" fill="#fff"/><path d="M11 5.5 7 9.5l4 4" stroke="#333" stroke-width="2" fill="none"/></svg>
<svg class="abs slide-arrow" style="left:533px" viewBox="0 0 19 19"><circle cx="9.5" cy="9.5" r="9.5" fill="#fff"/><path d="M8 5.5l4 4-4 4" stroke="#333" stroke-width="2" fill="none"/></svg>

<div class="abs cal-title">Event Calendar</div>
<div class="abs cal-head"><span class="arr">◀</span>August 2013<span class="arr">▶</span></div>
<div class="abs cal-days"><span>MON</span><span>TUE</span><span>WED</span><span>THU</span><span>FRI</span><span>SAT</span><span>SUN</span></div>
<div class="abs cal-grid">
  <div class="off">28</div><div>1</div><div>2</div><div>3</div><div class="today">4</div><div>5</div><div>6</div>
  <div>7</div><div>8</div><div>9</div><div>10</div><div>11</div><div>12</div><div>13</div>
  <div>14</div><div>15</div><div>16</div><div>17</div><div>18</div><div>19</div><div>20</div>
  <div>21</div><div>22</div><div>23</div><div>24</div><div>25</div><div>26</div><div>27</div>
  <div>28</div><div>29</div><div>30</div><div>31</div><div class="off">1</div><div class="off">2</div><div class="off">3</div>
</div>

<h2 class="abs" style="left:78px;top:392px">Welcome to Brisk Tutorium for Gifted Youth</h2>
<p class="abs copy" style="left:78px;top:420px;width:486px">We provide after-school enrichment programs in math, physics, chemistry, biology, and computer science, mentor middle and high school science research projects, and offer college counseling to aspiring students in pursuing their college dreams. Please explore this website to learn more about our programs and our approach to gifted education.</p>

<div class="abs card" style="left:78px"><h3><span class="ico"></span>eLearning</h3><p>Access our Online Learning Management System for current students and families.</p></div>
<div class="abs card" style="left:243px"><h3><span class="ico" style="background:#bbb"></span>Scheduler</h3><p>Online appointment for qualifying exams, gathering information, college counseling, or science research meetings</p></div>
<div class="abs card" style="left:407px"><h3><span class="ico" style="border-radius:50%"></span>Registration</h3><p>Click on Registration to sign up for our classes.</p></div>

<h2 class="abs" style="left:78px;top:621px">2013 - 2014 School Year Classes and Registration</h2>
<p class="abs copy" style="left:78px;top:648px;width:490px">The early registration deadline for returning students and summer camp participants is August 15.&nbsp; The open registration period is from August 15, 2013 - August 31, 2013. To register, click on the program title below. To learn more about class schedule, qualification, waiting list, and other information, click here.</p>
<div class="abs doc-link" style="top:713px"><svg width="16" height="18" viewBox="0 0 16 18"><path d="M2 1h8l4 4v12H2z" fill="#fff" stroke="#c33" stroke-width="1.4"/><path d="M4 12c3-6 5-6 8 0" stroke="#c33" fill="none" stroke-width="1.4"/></svg>Math Olympiad Classes</div>
<div class="abs doc-link" style="top:743px"><svg width="16" height="18" viewBox="0 0 16 18"><path d="M2 1h8l4 4v12H2z" fill="#fff" stroke="#c33" stroke-width="1.4"/><path d="M4 12c3-6 5-6 8 0" stroke="#c33" fill="none" stroke-width="1.4"/></svg>Physics, Chemistry, Computer Science, and Biology Olympiad Classes</div>

<div class="abs col-rule"></div>
<h2 class="abs" style="left:599px;top:393px">Latest News</h2>
<div class="abs news-nav">‹ ›</div>
<ul class="abs news">
  <li><a href="#">2013 College Matriculation List</a><time>2013-06-02</time></li>
  <li><a href="#">2013 College Matriculation List</a><time>2013-06-02</time></li>
  <li><a href="#">2013 College Matriculation List</a><time>2013-06-02</time></li>
  <li><a href="#">2013 College Matriculation List</a><time>2013-06-02</time></li>
</ul>
<div class="abs venue">
  <div class="venue-badge"></div>
  Westbrook University, 2210<br>Westbrook Lane, Irvine,<br>CA 92614-1187
  <a href="#" style="margin-top:5px">Maps to Brisk Tutorium, Irvine</a>
  <a href="#">Directions to Brisk Tutorium, Irvine</a>
</div>

<section class="abs why">
  <h2>Why Brisk Tutorium for Gifted Youth?</h2>
  <p>In 2006, Brisk Tutorium for Gifted Youth was the first academy to offer advanced math problem solving to gifted students in Orange County. With its roots in the Irvine math community and locations proximate to Harbor State University and Westbrook University, Brisk Tutorium for Gifted Youth combines California Standardized Mathematics Curriculum with math competitions and problem solving to help gifted students to discover their passion, develop their skills, and fulfill their college dreams. To learn more about our philosophy, history, statement of differentiation, and approach to gifted education, click here.</p>
</section>

<div class="abs reg-title">New Student Registration</div>
<div class="abs reg-note">Schedule a qualifying exam:<br>The program is designed to challenge gifted math students.</div>
<div class="abs reg-btn">REGISTER NOW <i>›</i></div>

<footer class="abs footer">
  <div class="f-col" style="left:70px">
    <h4>Related content</h4>
    <ul>
      <li>2013 Math Olympiad Summer Camp for Grades 5 - 6</li>
      <li>2013 Geometry and NumberQuest Bootcamp for Grades 7 - 8</li>
      <li>2013 Summit 12 Summer Bootcamp for Grades 10 - 11</li>
      <li>2013 Math Olympiad Summer Camp for Grades 3 - 4</li>
      <li>2013 Jump Start Algebra and Summit 8 Bootcamp for Grades 7 - 8</li>
      <li>2013 Summit 10 Summer Bootcamp for Grades 8 - 10</li>
    </ul>
  </div>
  <div class="f-rule" style="left:363px"></div>
  <div class="f-col" style="left:398px">
    <h4>Email Signup</h4>
    <div class="field">Name</div>
    <div class="field">Email ID</div>
    <div class="submit">SUBMIT</div>
  </div>
  <div class="f-rule" style="left:597px"></div>
  <div class="f-col" style="left:632px">
    <h4>Connect with us</h4>
    <ul class="social">
      <li><span class="sq"></span>Join with us on <b>Friendwall</b></li>
      <li><span class="sq" style="background:#4fb3e0"></span>Follow us on <b>Chirpline</b></li>
      <li><span class="sq" style="background:#2c6aa0"></span>Share on <b>Workweave</b></li>
      <li><span class="sq" style="background:#c43a30"></span>Watch on <b>Clipstream</b></li>
    </ul>
  </div>
</footer>
<div class="abs bottom-bar">Copyright © 2013 &nbsp;Brisk Tutorium for Gifted Youth. &nbsp;All rights reserved. &nbsp;&nbsp;| &nbsp;&nbsp;5820 Scholar Way, Suite 140 Irvine CA 92614. (949) 555-0137</div>
</body>
</html>
```